Broschüren-Design für Unternehmen aus dem Gesundheitsbereich
Zielgruppe
Wir sind ein Unternehmen aus dem Gesundheitsbereich und bieten wissenschaftlich fundierte Mikronährstoffanalysen (intravenöse Blutanalysen) an. Die Auswertung erfolgt mit Hilfe der weltweit einzigartigen Datenbank unseres wissenschaftlichen Leiters Prof. Dr. Torsten Halbach und beinhaltet zusätzliche eine individuelle Mikronährstoffempfehlung. Der Kunde kann unser Konzept in Form einer Analysebox (mit Materialien zur Entnahme von Blut- und Urinproben) bei uns erwerben. Es gibt verschiedene Analyseboxen in unterschiedlichem Umfang und Preisgestaltung zur Auswahl.
Unsere Zielgruppe sind gesundheitsbewusste Männer und Frauen im mittleren Alter („Gesundheitsmaximierer“).
Aufgabenstellung
8-12 Seiten, Format DIN A 5
Die Farbwahl bitte harmonisch an unser vorhandenes Logo / die angehängte Stylecard anpassen.
Die Neuauflage unserer Broschüre soll allgemeiner gehalten werden. Insbesondere die Titelseite (Bild sowie Headlines) der aktuellen Broschüre (siehe Upload) soll neugestaltet werden. Das Titelbild auf der Broschüre möchten wir gerne gegen allgemeineres Bildmaterial austauschen, z. B. mit Affinität zu unserem Logo oder zu den Themen Wissenschaft / Gesundheit / Mikronährstoffe. Seite 5 ('Die Analyse; Vier verschiedene Module') erfordert eine komplette Neugestaltung, da die angebotenen Analysemodule in der Form nicht mehr existieren. Wir haben neue themenspezifische Analyseboxen ins Leben gerufen (siehe Website: https://vitalquellnord.de/shop/), die wir allerdings nicht explizit in der Broschüre vorstellen möchten, damit die Broschüre bei möglichen Änderungen unseres Angebots künftig trotzdem immer aktuell bleibt. Aus diesem Grund wünschen wir uns für die Neuauflage der Broschüre durchweg allgemeingültige Formulierungen (Ohne Erwähnung von Namen oder Anzahl der angebotenen Analyseboxen).
Der Erklärfilm auf unserer Website verdeutlicht unser Konzept: https://www.videoportal-beispiel.de/watch?v=Qk3TzR8mLw2&feature=emb_title
Orientieren Sie sich gerne an den Creatives/Texten auf unserer Website.

```html
<!DOCTYPE html>
<html lang="de">
<head>
<meta charset="utf-8">
<title>Vitalquell Nord – Faltblatt</title>
<link href="https://fonts.googleapis.com/css2?family=Exo+2:wght@300;400&family=Open+Sans:wght@300;400;700&family=Montserrat:wght@400;600&display=swap" rel="stylesheet">
<style>
  :root{
    --teal:#63a9b8;
    --teal-dark:#4f98a8;
    --green:#86b451;
    --orange:#d78f27;
    --yellow:#e8b02a;
    --grey-bg:#f2f2f2;
    --ink:#454545;
    --white:#ffffff;
  }
  *{box-sizing:border-box;margin:0;padding:0}
  html,body{width:1198px;height:1200px;overflow:hidden;background:var(--white)}
  .canvas{position:relative;width:1198px;height:1200px}
  .brochure{position:absolute;left:0;top:172px;width:1198px;height:855px;display:flex}
  .panel{position:relative;width:399.33px;height:855px;overflow:hidden}
  .panel svg.bg{position:absolute;left:0;top:0}

  /* left panel */
  .panel--top3{background:var(--white)}
  .top3__label{position:absolute;left:40px;top:80px;font:300 21px "Exo 2",sans-serif;color:var(--yellow)}
  .top3__intro{position:absolute;left:39px;top:114px;width:270px;font:400 11.6px/14px "Montserrat",sans-serif;color:var(--white);letter-spacing:.2px}
  .top3__list{position:absolute;left:42px;top:214px;width:310px;list-style:none}
  .top3__item{position:relative;padding-left:26px;margin-bottom:23px;color:var(--white)}
  .top3__num{position:absolute;left:0;top:0;width:15px;height:15px;border-radius:50%;background:var(--white);color:#333;font:600 8px/15px "Montserrat",sans-serif;text-align:center}
  .top3__title{font:600 7.6px/10px "Montserrat",sans-serif;text-transform:uppercase;letter-spacing:.2px}
  .top3__text{font:400 6.6px/8.3px "Montserrat",sans-serif;margin-top:3px;width:210px}
  .top3__visual{position:absolute;left:0;top:410px;width:399px;height:366px;background:var(--grey-bg)}
  .top3__illustration{position:absolute;left:0;top:0;width:399px;height:366px;background:radial-gradient(ellipse at 45% 55%, #b7d3be 0%, #c9dde4 55%, var(--grey-bg) 80%)}
  .top3__box-icon{position:absolute;left:38px;top:766px}

  /* middle panel */
  .panel--info{background:var(--orange)}
  .info__title{position:absolute;left:0;width:399px;top:54px;text-align:center;font:400 22px "Exo 2",sans-serif;color:var(--teal)}
  .info__subtitle{position:absolute;left:0;width:399px;top:82px;text-align:center;font:400 17px "Open Sans",sans-serif;color:var(--green)}
  .info__body{position:absolute;left:54px;top:118px;width:299px;font:400 14.4px/18px "Open Sans",sans-serif;color:var(--ink);text-align:justify}
  .info__body p{margin-bottom:8px}
  .info__tubes{position:absolute;left:-36px;top:322px}
  .info__list{position:absolute;left:50px;top:490px;width:320px;list-style:none}
  .info__item{position:relative;height:58px;padding-left:54px}
  .info__item svg{position:absolute;left:0;top:4px}
  .info__item-title{font:700 7.8px/10px "Open Sans",sans-serif;color:var(--white);text-transform:uppercase}
  .info__item-text{font:400 6.6px/8.3px "Open Sans",sans-serif;color:var(--white);margin-top:4px;width:215px}
  .info__clipboard{position:absolute;left:300px;top:738px}

  /* right panel */
  .panel--cover{background:var(--teal)}
  .cover__headline{position:absolute;left:40px;top:130px;font:300 42px "Exo 2",sans-serif;color:var(--white);letter-spacing:.5px}
  .cover__tagline{position:absolute;left:40px;top:202px;font:300 18px "Open Sans",sans-serif;color:var(--white)}
  .cover__visual{position:absolute;left:7px;top:310px;width:351px;height:363px;background:var(--white);border-radius:0 175px 0 0;overflow:hidden}
  .cover__illustration{width:100%;height:100%;background:radial-gradient(ellipse at 50% 62%, #8fbcc6 0%, #d9b7b4 40%, #f4e4e2 65%, var(--white) 85%)}
  .cover__brand{position:absolute;left:65px;top:734px;width:253px;height:79px;background:var(--white);display:flex;align-items:center;justify-content:center;gap:10px}
  .cover__brand-dot{width:22px;height:22px;border-radius:50%;background:var(--teal)}
  .cover__brand-name{font:300 24px "Exo 2",sans-serif;color:var(--teal)}
</style>
</head>
<body>
<div class="canvas">
  <div class="brochure">

    <section class="panel panel--top3">
      <svg class="bg" width="400" height="410" viewBox="0 0 400 410">
        <rect width="400" height="410" fill="var(--green)"/>
        <path d="M118,0 C100,140 210,300 400,410 L400,0 Z" fill="var(--teal)"/>
      </svg>
      <div class="top3__label">TOP 3</div>
      <p class="top3__intro">Lorem ipsum dolor sit amet, consectetuer adipiscing elit, sed diam nonummy nibh euismod tincidunt ut laoreet dolore magna aliquam erat volutpat.sed diam nonummy nibh euismod tincidunt ut laoreet .</p>
      <ol class="top3__list">
        <li class="top3__item"><span class="top3__num">1</span><div class="top3__title">Lorem ipsum dolor sit amet, consectetuer adipisc</div><div class="top3__text">Lorem ipsum dolor sit amet, consectetuer adipiscing elit, sed diam nonummy nibh euismod tincidunt ut laoreet dolore magna aliquam erat volutpat.sed diam</div></li>
        <li class="top3__item"><span class="top3__num">2</span><div class="top3__title">Lorem ipsum dolor sit amet, consectetuer adipisc</div><div class="top3__text">Lorem ipsum dolor sit amet, consectetuer adipiscing elit, sed diam nonummy nibh euismod tincidunt ut laoreet dolore magna aliquam erat volutpat.sed diam</div></li>
        <li class="top3__item"><span class="top3__num">3</span><div class="top3__title">Lorem ipsum dolor sit amet, consectetuer adipisc</div><div class="top3__text">Lorem ipsum dolor sit amet, consectetuer adipiscing elit, sed diam nonummy nibh euismod tincidunt ut laoreet dolore magna aliquam erat volutpat.sed diam</div></li>
      </ol>
      <div class="top3__visual">
        <div class="top3__illustration" role="img" aria-label="Illustration: Forscher mit Lupe und Laborproben vor einem Balkendiagramm"></div>
      </div>
      <svg class="top3__box-icon" width="62" height="50" viewBox="0 0 62 50" aria-hidden="true">
        <path d="M10,22 L31,30 L52,22 L52,42 L31,49 L10,42 Z" fill="none" stroke="var(--teal)" stroke-width="2"/>
        <path d="M2,12 L22,4 L31,10 L40,4 L60,12 L52,20 L31,12 L10,20 Z" fill="var(--green)"/>
        <path d="M10,20 L31,28 L52,20 L31,12 Z" fill="var(--green)" opacity=".7"/>
      </svg>
    </section>

    <section class="panel panel--info">
      <svg class="bg" width="400" height="420" viewBox="0 0 400 420">
        <path d="M48,0 L356,0 C356,120 366,250 336,330 C300,420 100,425 66,340 C38,260 50,120 48,0 Z" fill="var(--white)"/>
      </svg>
      <h1 class="info__title">Mikronahrstoffversorgung</h1>
      <h2 class="info__subtitle">Optimal, nicht minimal</h2>
      <div class="info__body">
        <p>Nicht die minimale - sondern die optimale Miikronahrstoffversorgungist die Zukunft in der Vorsorge.</p>
        <p>Die individuelle Mikronahrstoffrezeptur dient zur Funktionserhaltung von Gesundheit und Therapie von Befindlichkeitsstörungen. Jeder kennt sie, die-kleineren oder grölseren - taglichen Befindlichkeiten. Seien es Verspannungen, Kopfschmerzen oder Antriebslosigkeit nach einer schlaflosen Nacht.</p>
      </div>
      <ul class="info__list">
        <li class="info__item">
          <svg width="40" height="40" viewBox="0 0 40 40"><g transform="rotate(-45 20 20)"><rect x="4" y="13" width="30" height="14" rx="3" fill="none" stroke="#fff" stroke-width="2.5"/><rect x="34" y="17" width="3" height="6" fill="#fff"/><rect x="7" y="16" width="6" height="8" fill="#fff"/></g></svg>
          <div class="info__item-title">Lorem ipsum dolor sit amet, consectetuer adipisc</div>
          <div class="info__item-text">Lorem ipsum dolor sit amet, consectetuer adipiscing elit, sed diam nonummy nibh euismod tincidunt ut laoreet dolore magna aliquam erat volutpat.sed diam</div>
        </li>
        <li class="info__item">
          <svg width="40" height="40" viewBox="0 0 40 40"><g transform="rotate(-45 20 20)"><rect x="4" y="13" width="30" height="14" rx="3" fill="none" stroke="#fff" stroke-width="2.5"/><rect x="34" y="17" width="3" height="6" fill="#fff"/><rect x="7" y="16" width="6" height="8" fill="var(--yellow)"/><rect x="14" y="16" width="6" height="8" fill="#fff"/></g></svg>
          <div class="info__item-title">Lorem ipsum dolor sit amet, consectetuer adipisc</div>
          <div class="info__item-text">Lorem ipsum dolor sit amet, consectetuer adipiscing elit, sed diam nonummy nibh euismod tincidunt ut laoreet dolore magna aliquam erat volutpat.sed diam</div>
        </li>
        <li class="info__item">
          <svg width="40" height="40" viewBox="0 0 40 40"><g transform="rotate(-45 20 20)"><rect x="4" y="13" width="30" height="14" rx="3" fill="none" stroke="#fff" stroke-width="2.5"/><rect x="34" y="17" width="3" height="6" fill="#fff"/><rect x="7" y="16" width="6" height="8" fill="var(--yellow)"/><rect x="14" y="16" width="6" height="8" fill="var(--green)"/><rect x="21" y="16" width="6" height="8" fill="#fff"/></g></svg>
          <div class="info__item-title">Lorem ipsum dolor sit amet, consectetuer adipisc</div>
          <div class="info__item-text">Lorem ipsum dolor sit amet, consectetuer adipiscing elit, sed diam nonummy nibh euismod tincidunt ut laoreet dolore magna aliquam erat volutpat.sed diam</div>
        </li>
        <li class="info__item">
          <svg width="40" height="40" viewBox="0 0 40 40"><g transform="rotate(-45 20 20)"><rect x="4" y="13" width="30" height="14" rx="3" fill="none" stroke="#fff" stroke-width="2.5"/><rect x="34" y="17" width="3" height="6" fill="#fff"/><rect x="7" y="16" width="6" height="8" fill="var(--yellow)"/><rect x="14" y="16" width="6" height="8" fill="var(--green)"/><rect x="21" y="16" width="5" height="8" fill="var(--teal)"/><rect x="27" y="16" width="5" height="8" fill="var(--teal-dark)"/></g></svg>
          <div class="info__item-title">Lorem ipsum dolor sit amet, consectetuer adipisc</div>
          <div class="info__item-text">Lorem ipsum dolor sit amet, consectetuer adipiscing elit, sed diam nonummy nibh euismod tincidunt ut laoreet dolore magna aliquam erat volutpat.sed diam</div>
        </li>
      </ul>
      <svg class="info__clipboard" width="70" height="80" viewBox="0 0 70 80" aria-hidden="true">
        <rect x="3" y="10" width="56" height="66" rx="4" fill="none" stroke="#fff" stroke-width="3"/>
        <rect x="20" y="4" width="22" height="10" rx="3" fill="none" stroke="#fff" stroke-width="3"/>
        <line x1="13" y1="28" x2="49" y2="28" stroke="#fff" stroke-width="3"/>
        <line x1="13" y1="40" x2="49" y2="40" stroke="#fff" stroke-width="3"/>
        <line x1="13" y1="52" x2="34" y2="52" stroke="#fff" stroke-width="3"/>
        <circle cx="52" cy="62" r="15" fill="#fff"/>
        <path d="M45,62 L50,67 L59,57" fill="none" stroke="var(--orange)" stroke-width="3"/>
      </svg>
      <svg class="info__tubes" width="70" height="70" viewBox="0 0 70 70" aria-hidden="true">
        <g fill="none" stroke="#fff" stroke-width="3" stroke-linecap="round">
          <path d="M28,10 L14,48 a7,7 0 0 0 13,5 L41,15"/><line x1="24" y1="9" x2="44" y2="16"/>
          <path d="M48,6 L36,44 a7,7 0 0 0 13,5 L61,11"/><line x1="44" y1="5" x2="64" y2="12"/>
        </g>
      </svg>
    </section>

    <section class="panel panel--cover">
      <svg class="bg" width="400" height="300" viewBox="0 0 400 300">
        <path d="M185,0 L400,0 L400,290 C300,250 190,150 185,0 Z" fill="var(--white)"/>
      </svg>
      <h1 class="cover__headline">ENDLICH</h1>
      <p class="cover__tagline">wieder im Leben stehen!</p>
      <div class="cover__visual">
        <div class="cover__illustration" role="img" aria-label="Illustration: Familie mit Kindern zwischen Pflanzen, von zwei schützenden Händen umrahmt"></div>
      </div>
      <div class="cover__brand">
        <span class="cover__brand-dot"></span>
        <span class="cover__brand-name">Vitalquell Nord</span>
      </div>
    </section>

  </div>
</div>
</body>
</html>
```